Quarvine, Cosmetic skin care line

I am not looking to change my logo quarvine on the label just want someone to design a different label I want it to be very classy as it is already just want something different. My product target classier people and people with higher income and for woman and men but mostly women. Looking to keep the label background black

Target Market(s)

Classier and higer income women/men mostly women

Industry/Entity Type

Cosmetics

• I don't really know

Colors

Designer to choose colors to be used in the design.

Requirements
Must have
• It must keep the same quarvine logo and the same matte black background color
Nice to have
• I want a different layout and maybe different fonts for the label
Should not have

```html
<!DOCTYPE html>
<html lang="en">
<head>
<meta charset="utf-8">
<title>Quarvine Eye Corrector Serum – Label Set</title>
<link rel="stylesheet" href="https://fonts.googleapis.com/css2?family=Amatic+SC:wght@700&family=Montserrat:wght@300;400&family=Yanone+Kaffeesatz:wght@700&display=swap">
<style>
  :root {
    --canvas: #ffffff;
    --label-black: #000000;
    --ink-white: #ffffff;
    --brand-blue: #1530e0;
    --art-tone: #2a2a2a;
  }
  * { box-sizing: border-box; margin: 0; padding: 0; }
  html, body {
    width: 1200px; height: 996px; overflow: hidden;
    background: var(--canvas);
  }
  .sheet { position: relative; width: 1200px; height: 996px; }

  .label {
    position: absolute;
    background: var(--label-black);
    color: var(--ink-white);
    overflow: hidden;
  }
  .label--front { left: 653px; top: 18px; width: 529px; height: 467px; }
  .label--bottle { left: 18px; top: 544px; width: 638px; height: 249px; }
  .label--jar { left: 18px; top: 800px; width: 1164px; height: 177px; }

  .flower-art {
    position: absolute;
    background: linear-gradient(180deg, var(--art-tone), #111111);
    border-radius: 2px;
  }
  .brand-name {
    position: absolute;
    font-family: "Amatic SC", cursive;
    font-weight: 700;
    color: var(--brand-blue);
    letter-spacing: 0.28em;
    line-height: 1;
    white-space: nowrap;
  }
  .tagline {
    position: absolute;
    font-family: "Amatic SC", cursive;
    font-weight: 700;
    color: var(--ink-white);
    letter-spacing: 0.22em;
    line-height: 1;
    white-space: nowrap;
  }

  .product-lockup {
    position: absolute;
    display: flex;
    align-items: flex-end;
    font-family: "Yanone Kaffeesatz", sans-serif;
    font-weight: 700;
    color: var(--brand-blue);
  }
  .product-initial { line-height: 0.8; }
  .product-stack { display: flex; flex-direction: column; align-items: flex-start; }
  .product-type {
    font-family: "Montserrat", sans-serif;
    font-weight: 300;
    color: var(--ink-white);
    line-height: 1;
    letter-spacing: -0.02em;
    white-space: nowrap;
    margin-left: 0.15em;
  }
  .product-rest { line-height: 0.62; letter-spacing: 0.04em; }

  .divider {
    position: absolute; left: 0; right: 0;
    height: 1px; background: var(--ink-white);
  }
  .claim {
    position: absolute; left: 0; right: 0;
    text-align: center;
    font-family: "Montserrat", sans-serif;
    font-weight: 400;
    line-height: 1.25;
    text-transform: uppercase;
  }

  /* Front panel */
  .label--front .flower-art { left: 53px; top: 44px; width: 142px; height: 308px; }
  .label--front .brand-name { left: 181px; top: 62px; font-size: 54px; }
  .label--front .tagline { left: 244px; top: 126px; font-size: 26px; }
  .label--front .product-lockup { left: 194px; bottom: 119px; font-size: 88px; }
  .label--front .product-type { font-size: 17.5px; margin-bottom: 6px; }
  .label--front .divider { top: 352px; }
  .label--front .claim { top: 372px; font-size: 20px; padding-left: 28px; }

  /* Bottle wrap */
  .label--bottle .flower-art { left: 205px; top: 23px; width: 77px; height: 165px; }
  .label--bottle .brand-name { left: 274px; top: 32px; font-size: 29px; }
  .label--bottle .tagline { left: 308px; top: 67px; font-size: 15px; }
  .label--bottle .product-lockup { left: 281px; bottom: 63px; font-size: 48px; }
  .label--bottle .product-type { font-size: 9.5px; margin-bottom: 3px; }
  .label--bottle .divider { top: 188px; }
  .label--bottle .claim { top: 198px; font-size: 11px; padding-left: 12px; }

  /* Jar wrap */
  .label--jar .flower-art { left: 469px; top: 17px; width: 54px; height: 117px; }
  .label--jar .brand-name { left: 522px; top: 7px; font-size: 36px; }
  .label--jar .tagline { left: 562px; top: 44px; font-size: 15px; }
  .label--jar .product-lockup { left: 522px; bottom: 45px; font-size: 60px; }
  .label--jar .product-type { font-size: 12.5px; margin-bottom: 4px; }
  .label--jar .divider { top: 134px; }
  .label--jar .claim { top: 140px; font-size: 8px; padding-left: 26px; }
</style>
</head>
<body>
<main class="sheet">

  <section class="label label--front">
    <div class="flower-art" role="img" aria-label="Single-line white drawing of a flower with two leaves on a long stem"></div>
    <div class="brand-name">QUARVINE</div>
    <div class="tagline">FOR ALL</div>
    <div class="product-lockup">
      <span class="product-initial">S</span>
      <span class="product-stack">
        <span class="product-type">EYE CORRECTOR</span>
        <span class="product-rest">erum</span>
      </span>
    </div>
    <div class="divider"></div>
    <p class="claim">With triple<br>peptides</p>
  </section>

  <section class="label label--bottle">
    <div class="flower-art" role="img" aria-label="Single-line white drawing of a flower with two leaves on a long stem"></div>
    <div class="brand-name">QUARVINE</div>
    <div class="tagline">FOR ALL</div>
    <div class="product-lockup">
      <span class="product-initial">S</span>
      <span class="product-stack">
        <span class="product-type">EYE CORRECTOR</span>
        <span class="product-rest">erum</span>
      </span>
    </div>
    <div class="divider"></div>
    <p class="claim">With triple<br>peptides</p>
  </section>

  <section class="label label--jar">
    <div class="flower-art" role="img" aria-label="Single-line white drawing of a flower with two leaves on a long stem"></div>
    <div class="brand-name">QUARVINE</div>
    <div class="tagline">FOR ALL</div>
    <div class="product-lockup">
      <span class="product-initial">S</span>
      <span class="product-stack">
        <span class="product-type">EYE CORRECTOR</span>
        <span class="product-rest">erum</span>
      </span>
    </div>
    <div class="divider"></div>
    <p class="claim">With triple<br>peptides</p>
  </section>

</main>
</body>
</html>
```